Whiskey label design and bottle design

We need a label design for our new whiskey company. We are going to use paper logo that can include any elements that the designer wants including shinny, glossy, etc. We need something eye catching that stands out. Our bottle has not been chosen so we are can use any type of bottle including a custom bottle. Something that looks expensive. High quality. Need to stand out. The Brand name for now is the Heart of Marrowdale

Target Market(s)

21 to 54 60% male, 40% female

Industry/Entity Type

Whiskey Spirits

Requirements
Must have
• Detailed packaging, A barcode for the SKU, Governement warning on the back, Area for a story on the back, size of bottle on the back, Cork Closure.
Nice to have
• Something with tradition, Quality, and it stands out from comeptors. High quality labels.

```html
<!DOCTYPE html>
<html lang="en">
<head>
<meta charset="utf-8">
<title>Heart of Marrowdale – Premium Wisky Label</title>
<link rel="stylesheet" href="https://fonts.googleapis.com/css2?family=Oswald:wght@400;500;600&family=Roboto+Condensed:wght@400;700&display=swap">
<style>
  :root {
    --backdrop: #d4d4d4;
    --label-black: #141414;
    --label-edge: #2a2a2a;
    --band-white: #f4f4f4;
    --brand-red: #8e1b22;
    --ink-white: #ffffff;
    --ink-soft: #cfcfcf;
  }
  * { box-sizing: border-box; margin: 0; padding: 0; }
  html, body {
    width: 1200px;
    height: 1200px;
    overflow: hidden;
    background: var(--backdrop);
  }
  .canvas {
    position: relative;
    width: 1200px;
    height: 1200px;
    background: var(--backdrop);
  }
  .label {
    position: absolute;
    left: 340px;
    top: 90px;
    width: 520px;
    height: 1020px;
    background: var(--label-black);
    border: 2px solid var(--label-edge);
    overflow: hidden;
    color: var(--ink-white);
    text-align: center;
  }
  .brand-mark {
    position: absolute;
    top: 215px;
    left: 0;
    width: 100%;
    display: flex;
    align-items: center;
    justify-content: center;
    gap: 14px;
  }
  .brand-mark__dot {
    width: 22px;
    height: 22px;
    border-radius: 50%;
    background: var(--ink-white);
    flex: none;
  }
  .brand-mark__name {
    font-family: "Oswald", sans-serif;
    font-weight: 500;
    font-size: 32px;
    letter-spacing: 0.5px;
    color: var(--ink-white);
    text-transform: uppercase;
    white-space: nowrap;
  }
  .name-band {
    position: absolute;
    left: -110px;
    top: 475px;
    width: 740px;
    height: 104px;
    background: var(--band-white);
    transform: rotate(-20deg);
    display: flex;
    align-items: center;
    justify-content: center;
  }
  .name-band__title {
    font-family: "Oswald", sans-serif;
    font-weight: 600;
    font-size: 50px;
    color: var(--brand-red);
    white-space: nowrap;
  }
  .product-info {
    position: absolute;
    left: 0;
    top: 745px;
    width: 100%;
    font-family: "Roboto Condensed", sans-serif;
  }
  .product-info__type {
    font-family: "Oswald", sans-serif;
    font-weight: 400;
    font-size: 34px;
    letter-spacing: 1px;
    text-transform: uppercase;
  }
  .product-info__origin {
    margin-top: 14px;
    font-weight: 700;
    font-size: 18px;
    letter-spacing: 0.5px;
    text-transform: uppercase;
  }
  .product-info__origin-fr {
    margin-top: 6px;
    font-size: 13px;
    color: var(--ink-soft);
    text-transform: uppercase;
  }
  .product-info__volume {
    margin-top: 32px;
    font-size: 17px;
    letter-spacing: 0.5px;
    color: var(--ink-soft);
  }
</style>
</head>
<body>
  <main class="canvas">
    <section class="label">
      <div class="brand-mark">
        <span class="brand-mark__dot"></span>
        <p class="brand-mark__name">Heart of Marrowdale</p>
      </div>

      <div class="name-band">
        <h1 class="name-band__title">Heart of Marrowdale</h1>
      </div>

      <div class="product-info">
        <p class="product-info__type">Premium Wisky</p>
        <p class="product-info__origin">Distilled and bottled in Kentucky</p>
        <p class="product-info__origin-fr">Distillé et embouteillé au Canada</p>
        <p class="product-info__volume">40% ALC / VOL 750 ML</p>
      </div>
    </section>
  </main>
</body>
</html>
```